Brackenford Group Website

We have a newly established brand for a company with an existing portfolio of property. The company is corporate and professional and both owns and develops property. The website should reflect a professional and stable organisation. The website should showcase the existing properties (6), have a home page that describes the company and its activities and has a "about us" page. The website will be in Wordpress and we would like the code for all pages to be sent to us by the successful designer upon completion of the job.
Updates

sorry was called from the office on an urgent matter. To be fair on submitters, i need a couple more days to finalise reviews.

Contact Information for Business Card

Brackenford Logo on front
Black background with silver logo.

Coding

Number of Pages Required

Colors

Designer to choose colors to be used in the design.

Requirements
Must have
• Text side of card should include
• Brackenford Property Group (as title in logo font)
• Employee Name (centered)
• Job Title (centered below name)
• Address 4 lines
• Email, mobile office phone, 3 lines
• website address (probably as footer)

```html
<!DOCTYPE html>
<html lang="en">
<head>
<meta charset="utf-8">
<title>Brackenford Property Group</title>
<link rel="stylesheet" href="https://fonts.googleapis.com/css2?family=Lato:wght@300;400;700&display=swap">
<style>
:root{
  --navy:#13295b;
  --navy-deep:#0c1d45;
  --accent:#e6e51e;
  --text:#4a4a4a;
  --muted:#6b6b6b;
  --paper:#f5f5f5;
  --line:#5a5a5a;
  --dot:#c9ccd2;
}
*{box-sizing:border-box;margin:0;padding:0}
html,body{width:1200px;height:2758px;overflow:hidden}
body{font-family:'Lato',sans-serif;color:var(--text);background:var(--paper);position:relative}
.abs{position:absolute}
.center{text-align:center}
.section{position:absolute;left:0;width:1200px}
.section-title{position:absolute;left:0;width:1200px;text-align:center;font-size:24px;font-weight:400;color:var(--navy);letter-spacing:.2px}
.btn{position:absolute;display:flex;align-items:center;justify-content:center;border:1px solid var(--line);font-size:11px;letter-spacing:.8px;color:#333;background:transparent}
.dots{position:absolute;left:0;width:1200px;display:flex;justify-content:center;gap:7px}
.dots span{width:11px;height:11px;border-radius:50%;background:var(--dot)}
.dots span.on{background:var(--navy-deep)}

/* hero */
.hero{top:0;height:564px;background:linear-gradient(160deg,#1d3a78 0%,#14306a 45%,#0f2760 100%)}
.brand{left:150px;top:72px;width:160px;text-align:center;color:#fff}
.brand-name{font-size:19px;letter-spacing:2.4px;font-weight:400;display:flex;align-items:center;justify-content:center;gap:6px}
.brand-name i{width:8px;height:8px;background:#fff;display:inline-block}
.brand-rule{height:1px;background:#fff;margin:8px 0 7px}
.brand-sub{font-size:11px;letter-spacing:2px}
.nav{right:150px;top:74px;display:flex;gap:26px;color:#fff;font-size:11.5px;letter-spacing:.3px}
.top-icons{right:150px;top:31px;display:flex;gap:8px;align-items:center}
.top-icons span{width:10px;height:10px;border-radius:50%;border:1px solid #fff}
.headline{left:0;top:238px;width:1200px;text-align:center;color:#fff;font-size:34px;font-weight:300;line-height:42px}
.headline em{font-style:normal;color:var(--accent)}
.hero .btn{border-color:#fff;color:#fff;top:351px;height:33px;width:115px;font-size:12px}

/* about */
.about{top:564px;height:406px;background:var(--paper)}
.about-text{left:190px;width:820px;top:136px;font-size:13px;line-height:18.5px;color:#444;text-align:center;font-weight:300}
.about-text p{margin-bottom:9px}

/* expertise */
.expertise{top:970px;height:533px;background:linear-gradient(180deg,#e7ebf1 0%,#eef1f5 50%,#e4e9f0 100%)}
.card-img{position:absolute;width:212px;height:196px}
.card-title{position:absolute;width:230px;text-align:center;font-size:12.5px;font-weight:700;color:#222;letter-spacing:.2px;line-height:15px}
.card-text{position:absolute;width:212px;text-align:center;font-size:11px;line-height:15px;color:#555;font-weight:300}

/* case studies */
.cases{top:1503px;height:390px;background:var(--paper)}
.case-img{position:absolute;width:292px;height:141px}
.case-title{position:absolute;font-size:14px;color:#222;letter-spacing:.2px}
.case-text{position:absolute;width:220px;font-size:11px;line-height:15px;color:#555;font-weight:300}
.case-arrow{position:absolute;width:32px;height:30px;background:#dcdee2;display:flex;align-items:center;justify-content:center}
.case-arrow.on{background:var(--navy-deep)}

/* team */
.team{top:1893px;height:532px;background:var(--paper)}
.photo{position:absolute;width:289px;height:247px;border:1px solid #e1e1e1;background:#fff}
.photo div{position:absolute;left:30px;right:30px;bottom:0;top:0;background:linear-gradient(180deg,#f3f3f3 0%,#d9d2c8 45%,#2a2c31 100%)}
.member{position:absolute;width:289px;text-align:center}
.member .role{font-size:11px;color:#666;font-weight:300}
.member .name{font-size:15px;color:#222;margin-top:6px;letter-spacing:.3px}
.member .bio{font-size:11px;line-height:14px;color:#555;font-weight:300;margin:6px auto 0;width:250px}
.socials{position:absolute;width:289px;display:flex;justify-content:center;gap:4px}
.socials span{width:24px;height:24px;border-radius:50%;border:1px solid #9a9a9a}

/* contact */
.contact{top:2425px;height:333px;background:linear-gradient(180deg,#f0f2f5 0%,#e5e9ef 60%,#dde2ea 100%)}
.contact-line{position:absolute;left:0;width:1200px;text-align:center;font-size:11.5px;color:#333;font-weight:300}
.contact-icon{position:absolute;left:586px}
</style>
</head>
<body>

<header class="section hero" role="img" aria-label="Night view of tall glass office towers in a blue tint">
  <div class="abs brand">
    <div class="brand-name"><i></i>BRACKENFORD</div>
    <div class="brand-rule"></div>
    <div class="brand-sub">PROPERTY GROUP</div>
  </div>
  <div class="abs top-icons" aria-hidden="true">
    <svg width="11" height="11" viewBox="0 0 11 11"><circle cx="4.5" cy="4.5" r="3.5" fill="none" stroke="#fff" stroke-width="1.2"/><line x1="7" y1="7" x2="10" y2="10" stroke="#fff" stroke-width="1.2"/></svg>
    <span></span><span></span><span></span><span></span>
  </div>
  <nav class="abs nav">
    <span>HOME</span><span>ABOUT</span><span>EXPERTISE</span><span>CASE STUDIES</span><span>TEAM</span><span>CONTACT US</span>
  </nav>
  <h1 class="abs headline">A PREMIER <em>INSTITUTIONAL</em> REAL ESTATE FIRM<br>WITH AN <em>ENTREPRENEURIAL</em> ADVANTAGE</h1>
  <div class="btn" style="left:462px">EXPERTISE</div>
  <div class="btn" style="left:605px">CONTACT US</div>
  <svg class="abs" style="left:580px;top:490px" width="40" height="22" viewBox="0 0 40 22"><polyline points="1,1 20,20 39,1" fill="none" stroke="#9fb0d0" stroke-width="1.5"/><polyline points="8,1 20,13 32,1" fill="none" stroke="#9fb0d0" stroke-width="1"/></svg>
</header>

<section class="section about">
  <h2 class="section-title" style="top:89px">ABOUT BRACKENFORD</h2>
  <div class="abs about-text">
    <p>Brackenford Group is a privately-owned commercial real estate investment company founded in Auckland in 2007. Working with a small group of long-standing private and institutional partners, the firm has successfully acquired and developed assets valued at over $1.0 billion.</p>
    <p>Brackenford Group has a long track record of success in the acquisition, consenting, development, renovation and repositioning of office, tourism accommodation, residential, social housing, retail and mixed use properties within the Auckland region.</p>
    <p>Drawing upon the decades of experience of its principals, partners and the skill sets of the Brackenford team, the company has been able to identify many successful real estate investment opportunities, produce exceptional investment performance and provide lasting positive impacts on the tenants and communities it serves.</p>
  </div>
  <div class="btn" style="left:515px;top:315px;width:162px;height:36px;font-size:12px">LEARN MORE</div>
</section>

<section class="section expertise">
  <h2 class="section-title" style="top:42px">OUR EXPERTISE</h2>

  <div class="card-img" style="left:150px;top:107px;background:linear-gradient(180deg,#3d6fc2,#8aa0b8 60%,#5b5348)" role="img" aria-label="Skyscrapers seen from street level against blue sky"></div>
  <div class="card-img" style="left:376px;top:107px;background:linear-gradient(180deg,#6b513a,#cfc6b8 50%,#8b6a48)" role="img" aria-label="People reviewing charts on a wooden table"></div>
  <div class="card-img" style="left:606px;top:107px;background:linear-gradient(180deg,#e9ecef,#cfd3d6 60%,#c7b24a)" role="img" aria-label="Building model with construction cranes"></div>
  <div class="card-img" style="left:837px;top:107px;background:linear-gradient(180deg,#d9dde2,#9a6a4e 60%,#6e3e2c)" role="img" aria-label="Renovated office lobby with brick floor"></div>

  <div class="card-title" style="left:141px;top:322px">ACQUISITIONS</div>
  <div class="card-title" style="left:363px;top:322px">RESOURCE MANAGEMENT<br>PLANNING AND CONSENTING</div>
  <div class="card-title" style="left:593px;top:322px">DEVELOPMENT</div>
  <div class="card-title" style="left:828px;top:322px">RENOVATION AND REPOSITIONING</div>

  <div class="card-text" style="left:150px;top:360px">Prior to any successful real estate acquisition we plan and implement proactive and thoughtful market and asset research</div>
  <div class="card-text" style="left:376px;top:360px">The Brackenford team is able to obtain complex development consents by working closely with the city and key...</div>
  <div class="card-text" style="left:606px;top:360px">With expertise in the development of office, tourism accommodation, hospitality, retail, residential, social housing...</div>
  <div class="card-text" style="left:837px;top:360px">Brackenford focuses on recognizing the unrealized value of existing, underperforming assets and successfully executing...</div>

  <div class="btn" style="left:193px;top:421px;width:114px;height:28px">LEARN MORE</div>
  <div class="btn" style="left:419px;top:421px;width:114px;height:28px">LEARN MORE</div>
  <div class="btn" style="left:649px;top:421px;width:114px;height:28px">LEARN MORE</div>
  <div class="btn" style="left:880px;top:421px;width:114px;height:28px">LEARN MORE</div>

  <div class="dots" style="top:490px"><span></span><span class="on"></span><span></span></div>
</section>

<section class="section cases">
  <h2 class="section-title" style="top:42px">CASE STUDIES</h2>

  <div class="case-img" style="left:150px;top:101px;background:linear-gradient(160deg,#2b3440,#6f7d8c 55%,#d7dde2)" role="img" aria-label="Dark glass office towers against a pale sky"></div>
  <div class="case-img" style="left:454px;top:101px;background:linear-gradient(90deg,#eef1f3,#d8c7b5 45%,#4e5663)" role="img" aria-label="Open hand holding a small model of buildings"></div>
  <div class="case-img" style="left:758px;top:101px;background:linear-gradient(180deg,#5d7fb0,#8a8fa0 45%,#4f4b4a)" role="img" aria-label="Two storey family house at dusk"></div>

  <div class="case-title" style="left:150px;top:257px">ASHCOMBE</div>
  <div class="case-title" style="left:454px;top:257px">THE WEXLEY</div>
  <div class="case-title" style="left:758px;top:257px">FERNLEIGH</div>

  <div class="case-text" style="left:150px;top:282px">Riverside development between the old mill and the civic hall..</div>
  <div class="case-text" style="left:454px;top:282px">Riverside development between the old mill and the civic hall..</div>
  <div class="case-text" style="left:758px;top:282px">Riverside development between the old mill and the civic hall..</div>

  <div class="case-arrow" style="left:407px;top:284px"><svg width="8" height="10" viewBox="0 0 8 10"><polyline points="2,1 6,5 2,9" fill="none" stroke="#555" stroke-width="1"/></svg></div>
  <div class="case-arrow on" style="left:710px;top:284px"><svg width="8" height="10" viewBox="0 0 8 10"><polyline points="2,1 6,5 2,9" fill="none" stroke="#fff" stroke-width="1"/></svg></div>
  <div class="case-arrow" style="left:1014px;top:284px"><svg width="8" height="10" viewBox="0 0 8 10"><polyline points="2,1 6,5 2,9" fill="none" stroke="#555" stroke-width="1"/></svg></div>

  <div class="dots" style="top:356px"><span></span><span class="on"></span><span></span></div>
</section>

<section class="section team">
  <h2 class="section-title" style="top:47px">MEET OUR EXPERT TEAM</h2>

  <div class="photo" style="left:150px;top:105px"><div role="img" aria-label="Portrait of a team member in a dark suit"></div></div>
  <div class="photo" style="left:455px;top:105px"><div role="img" aria-label="Portrait of a team member in a dark suit"></div></div>
  <div class="photo" style="left:761px;top:105px"><div role="img" aria-label="Portrait of a team member in a dark suit"></div></div>

  <div class="member" style="left:150px;top:371px">
    <div class="role">(Sr. Advisor)</div>
    <div class="name">MILES HARTWELL</div>
    <div class="bio">20-30 word summary A leading manager in the xxxxxxxxx</div>
  </div>
  <div class="member" style="left:455px;top:370px">
    <div class="role">(Director)</div>
    <div class="name">OWEN RADLEY-MARSH</div>
    <div class="bio">Founder of Brackenford with many years of asset and development management experience across numerous real estate sectors</div>
  </div>
  <div class="member" style="left:761px;top:370px">
    <div class="role">(Director)</div>
    <div class="name">ETHAN PRYCE</div>
    <div class="bio">20-30 word summary A leading manager in the xxxxxxxxx</div>
  </div>

  <div class="socials" style="left:150px;top:469px"><span></span><span></span><span></span><span></span></div>
  <div class="socials" style="left:455px;top:469px"><span></span><span></span><span></span><span></span></div>
  <div class="socials" style="left:761px;top:469px"><span></span><span></span><span></span><span></span></div>
</section>

<section class="section contact" role="img" aria-label="Faint city skyline in the background">
  <h2 class="section-title" style="top:45px;left:10px">CONTACT US</h2>

  <svg class="contact-icon" style="top:104px" width="26" height="24" viewBox="0 0 26 24"><path d="M13 2a6 6 0 0 0-6 6c0 5 6 10 6 10s6-5 6-10a6 6 0 0 0-6-6z" fill="none" stroke="#333" stroke-width="1.2"/><circle cx="13" cy="8" r="2.2" fill="none" stroke="#333" stroke-width="1.2"/><polyline points="5,16 2,22 24,22 21,16" fill="none" stroke="#333" stroke-width="1.2"/></svg>
  <div class="contact-line" style="top:138px">Brackenford Group Ltd &nbsp;Level 4, Harbourview House, 18 Kestrel Lane, Auckland CBD, PO Box 2207, Auckland 1140</div>

  <svg class="contact-icon" style="top:178px" width="26" height="24" viewBox="0 0 26 24"><path d="M6 3l4 0 2 5-3 2c1 3 3 5 6 6l2-3 5 2 0 4c-1 1-2 2-4 2C10 21 3 14 3 7c0-2 2-4 3-4z" fill="none" stroke="#333" stroke-width="1.2"/></svg>
  <div class="contact-line" style="top:204px">+64 9 555 0184</div>

  <svg class="contact-icon" style="top:242px" width="26" height="22" viewBox="0 0 26 22"><rect x="2" y="5" width="22" height="15" fill="none" stroke="#333" stroke-width="1.2"/><polyline points="2,5 13,14 24,5" fill="none" stroke="#333" stroke-width="1.2"/><line x1="8" y1="2" x2="18" y2="2" stroke="#333" stroke-width="1.2"/></svg>
  <div class="contact-line" style="top:268px">miles@brackenfordgroup.co.nz</div>
</section>

</body>
</html>
```